Website Design Layout for Selling Digital Artwork

***I am looking for a unique website design layout. Please do not submit modified wordpress themes/templates***

I need a website design for showing off and selling digital art work from an independent artist (see samples in the attached document).

The art is of landscapes and portraits, mostly celebrity portraits.

The design should have;

1. a main page where I can show off some of the art work

2. A gallery page where I can display all of the different artwork

3. A simple blog layout where I can talk about art philosophy

The website should NOT include a search field.

Since website is for an independent artist, it should reflect that in the design. An elegant, simple and clean design.

Number of Pages Required

3 page

Colors

Designer to choose colors to be used in the design.

Requirements
Should not have
• A search field

```html
<!DOCTYPE html>
<html lang="en">
<head>
<meta charset="utf-8">
<title>Easel Room</title>
<link rel="stylesheet" href="https://fonts.googleapis.com/css2?family=Nunito+Sans:wght@400;600;700;800&display=swap">
<style>
  :root{
    --ink:#111111;
    --text:#2a2a2a;
    --muted:#555555;
    --white:#ffffff;
    --panel:#eff0f5;
    --cream:#fcfaeb;
    --black:#000000;
    --footer-text:#bdbdbd;
    --rule:#d8d8de;
  }
  *{box-sizing:border-box;margin:0;padding:0}
  html,body{width:1200px;height:3435px;overflow:hidden}
  body{position:relative;background:var(--white);color:var(--text);font-family:"Nunito Sans",Arial,sans-serif}
  .abs{position:absolute}

  /* header */
  .site-header{left:0;top:0;width:1200px;height:69px;background:var(--white)}
  .brand{left:94px;top:22px;font-size:20px;font-weight:700;letter-spacing:4px;color:var(--ink);text-transform:uppercase}
  .main-nav a{position:absolute;top:26px;font-size:15px;font-weight:600;color:var(--ink);text-decoration:none}

  /* hero */
  .hero-art{left:0;top:69px;width:1200px;height:531px;
    background:linear-gradient(120deg,#1d5a4a 0%,#a3161b 30%,#c94a2a 48%,#7a1420 62%,#c7c4d8 80%,#245e55 100%)}

  /* intro */
  .intro-title{left:149px;top:700px;width:380px;font-size:43px;line-height:46px;font-weight:800;color:var(--ink)}
  .intro-rule{left:151px;top:867px;width:129px;height:2px;background:var(--ink)}
  .intro-copy{left:575px;top:698px;width:490px;font-size:15.5px;line-height:22px;color:var(--text)}

  /* latest sale */
  .sale-panel{left:238px;top:1003px;width:962px;height:509px;background:var(--panel)}
  .sale-art{left:92px;top:1060px;width:393px;height:396px;border:3px solid var(--ink);
    background:radial-gradient(circle at 50% 45%,#d8d8d8 0%,#8a8a8a 45%,#2b2b2b 100%)}
  .sale-rule{left:536px;top:1131px;width:98px;height:2px;background:var(--ink)}
  .sale-title{left:657px;top:1104px;width:460px;font-size:43px;line-height:46px;font-weight:700;color:var(--ink)}
  .sale-copy{left:586px;top:1228px;width:430px;font-size:14.5px;line-height:22px;color:var(--text)}
  .slider-controls{left:584px;top:1328px;width:100px;height:42px}

  /* collection */
  .collection{left:0;top:1512px;width:1200px;height:961px;background:var(--cream)}
  .portrait{position:absolute;border:3px solid var(--ink);background:linear-gradient(160deg,#e6e6e6 0%,#9d9d9d 55%,#4a4a4a 100%)}
  .portrait--colour{background:linear-gradient(160deg,#dfe3ea 0%,#d99a6a 40%,#1f2b4a 100%)}
  .collection-title{left:103px;top:2196px;font-size:41px;font-weight:800;color:var(--ink)}
  .btn{position:absolute;display:flex;align-items:center;justify-content:center;border:2px solid var(--ink);border-radius:30px;font-size:14px;font-weight:700;color:var(--ink);background:transparent}

  /* blog */
  .post-card{position:absolute;top:2553px;width:494px;height:298px;background:var(--panel)}
  .post-art{position:absolute;left:0;top:0;width:247px;height:298px;
    background:linear-gradient(150deg,#ffffff 0%,#c9b9d6 40%,#2b3a6a 75%,#f2f2f2 100%)}
  .post-title{position:absolute;left:265px;top:80px;width:200px;font-size:15px;line-height:23px;font-weight:600;color:var(--ink)}
  .post-rule{position:absolute;left:265px;top:165px;width:210px;height:1px;background:var(--rule)}
  .post-date{position:absolute;left:265px;top:178px;font-size:12px;font-weight:700;color:var(--muted)}
  .blog-title{left:0;top:2888px;width:1200px;text-align:center;font-size:41px;font-weight:800;color:var(--ink)}

  /* footer */
  .site-footer{left:0;top:3068px;width:1200px;height:367px;background:var(--black);color:var(--footer-text)}
  .footer-brand{left:94px;top:82px;font-size:20px;font-weight:700;letter-spacing:4px;color:var(--white);text-transform:uppercase}
  .footer-about{left:94px;top:120px;width:420px;font-size:14px;line-height:20px}
  .social{left:94px;top:224px;display:flex;gap:22px}
  .social span{display:block;width:11px;height:11px;border-radius:50%;background:var(--white)}
  .footer-contact{left:611px;top:109px;font-size:15px;line-height:26px;font-style:normal;color:var(--footer-text)}
  .footer-links{left:953px;top:109px;list-style:none;font-size:14px;line-height:25px}
  .footer-links li::before{content:"›";margin-right:8px;color:var(--white)}
  .footer-rule{left:0;top:294px;width:1200px;height:1px;background:#222}
  .copyright{left:0;top:320px;width:1200px;text-align:center;font-size:13px}
</style>
</head>
<body>

<header class="abs site-header">
  <div class="abs brand">Easel Room</div>
  <nav class="main-nav">
    <a style="left:653px">Home</a>
    <a style="left:753px">Work Gallery</a>
    <a style="left:905px">Our Blog</a>
    <a style="left:1028px">Contact Us</a>
  </nav>
</header>

<div class="abs hero-art" role="img" aria-label="Hero artwork: portrait of a woman with vivid red, green and violet body paint"></div>

<section>
  <h1 class="abs intro-title">Providing high quality original fine art collection</h1>
  <div class="abs intro-rule"></div>
  <p class="abs intro-copy">This is Canvasly's version of Lorem Ipsum. Proin gravida nibh vel velit auctor aliquet. Aenean sollicitudin, lorem quis bibendum auctor, nisi elit consequat ipsum, nec sagittis sem nibh id elit. Duis sed odio sit amet nibh vulputate cursus a sit amet mauris. Morbi accumsan ipsum velit. Nam nec tellus a odio tincidunt auctor a ornare odio.<br>Sed non mauris vitae erat consequat auctor eu in elit. Class aptent taciti sociosqu ad litora torquent per conubia nostra, per inceptos himenaeos. Mauris in erat justo.</p>
</section>

<section>
  <div class="abs sale-panel"></div>
  <div class="abs sale-art" role="img" aria-label="Featured artwork: black and white sketch-style portrait"></div>
  <div class="abs sale-rule"></div>
  <h2 class="abs sale-title">Check out the latest art sale collections</h2>
  <p class="abs sale-copy">We works on a wide variety of art &amp; painting designs every day. We deliver quality designs based on our boundless creativity and your needs.</p>
  <svg class="abs slider-controls" viewBox="0 0 100 42" aria-label="Slider controls">
    <circle cx="21" cy="21" r="19" fill="none" stroke="#111" stroke-width="2"/>
    <polyline points="24,14 17,21 24,28" fill="none" stroke="#111" stroke-width="2"/>
    <circle cx="73" cy="21" r="19" fill="none" stroke="#111" stroke-width="2"/>
    <polyline points="70,14 77,21 70,28" fill="none" stroke="#111" stroke-width="2"/>
  </svg>
</section>

<section class="abs collection">
  <div class="portrait portrait--colour" style="left:94px;top:109px;width:229px;height:227px" role="img" aria-label="Colour portrait artwork"></div>
  <div class="portrait" style="left:355px;top:109px;width:229px;height:227px" role="img" aria-label="Pencil-style portrait artwork"></div>
  <div class="portrait" style="left:614px;top:109px;width:229px;height:227px" role="img" aria-label="Pencil-style portrait artwork"></div>
  <div class="portrait" style="left:877px;top:109px;width:229px;height:227px" role="img" aria-label="Pencil-style portrait artwork"></div>
  <div class="portrait" style="left:94px;top:377px;width:233px;height:264px" role="img" aria-label="Pencil-style portrait artwork"></div>
  <div class="portrait" style="left:350px;top:377px;width:234px;height:264px" role="img" aria-label="Pencil-style portrait artwork"></div>
  <div class="portrait" style="left:611px;top:382px;width:495px;height:492px" role="img" aria-label="Large sketch-style portrait artwork"></div>
</section>
<h2 class="abs collection-title">Explore the Collection</h2>
<div class="btn" style="left:218px;top:2285px;width:155px;height:46px">View all</div>

<section>
  <article class="post-card" style="left:92px">
    <div class="post-art" role="img" aria-label="Blog artwork: watercolour portrait of a woman"></div>
    <h3 class="post-title">10 Steps: How to Create a Successful Business From Your Art</h3>
    <div class="post-rule"></div>
    <div class="post-date">Posted on : Jan 01, 2018</div>
  </article>
  <article class="post-card" style="left:612px">
    <div class="post-art" role="img" aria-label="Blog artwork: watercolour portrait of a woman"></div>
    <h3 class="post-title">10 Steps: How to Create a Successful Business From Your Art</h3>
    <div class="post-rule"></div>
    <div class="post-date">Posted on : Jan 01, 2018</div>
  </article>
  <h2 class="abs blog-title">Latest Blog Posts</h2>
  <div class="btn" style="left:522px;top:2958px;width:156px;height:44px">View all</div>
</section>

<footer class="abs site-footer">
  <div class="abs footer-brand">Easel Room</div>
  <p class="abs footer-about">Morbi odio eros, volutpat ut pharetra vitae, lobortis sed nibh. Donec sed odio operae, eu vulputate felis rhoncus. Quo usque tandem abutere, Catilina, patientia nostra? Etiam habebis sem dicantur.</p>
  <div class="abs social" aria-label="Social links"><span></span><span></span><span></span><span></span></div>
  <address class="abs footer-contact">Easel Room<br>12 Linden Row, Bristol<br>Tel: 01632-960418</address>
  <ul class="abs footer-links">
    <li>Home</li>
    <li>Work Gallery</li>
    <li>Our Blog</li>
    <li>Contact Us</li>
  </ul>
  <div class="abs footer-rule"></div>
  <div class="abs copyright">Easel Room © 2019. Privacy Policy</div>
</footer>

</body>
</html>
```